IT Services Company Needs Corporate PPT Template

This is urgent (need a fast turn around). We need a corporate PPT template deck (NOTE: Deck should be in 4:3 ratio) for our IT Services firm that is clean but slick and modern. We tend to lean more towards the flat design look. I'm attaching a zip file which includes our Corporate Branding Guide (which is in progress), color scheme, A PPT deck as inspiration (our logo is on the last slide), our font (LATO). Our newly launched website is located at: http://www.veltrani.com.

As an example of a deck we like see: http://stockpanel.net/item/clean-multipurpose-business-presentation-template/5218830?WT.ac=category_thumb&WT.seg_1=category_thumb&WT.z_author=BrimLayouts
Although we don't want "this" deck - it gives an idea of style.

I'm also attaching a copy of our corporate deck as it is now to give you an idea of the type of content that would appear on various slides. We definitely want the following slides (at least) within the template:

Title Slide
Blank Slide
2 Column - with bullets
2 Column - no bullets
Single Column - no bullets
Single Column - with bullets
Various Charts and Tables (see example deck)
Meet the Team
Offering Slide
Customer Showcase
Timeline
Case Study
Contact US

Note: Being awarded this job will lead to a second job of creating our corporate deck.

CIO, CEO, Technology Officers, Sales People, Marketing, IT heads and staff, Customers, Prospective customers

Business

• See description and attached files

```html
<!DOCTYPE html>
<html lang="en">
<head>
<meta charset="utf-8">
<title>Single Column Bulleted List – Veltrani</title>
<link rel="stylesheet" href="https://fonts.googleapis.com/css2?family=Lato:wght@300;400;700;900&display=swap">
<style>
  :root {
    --navy: #1b3d6b;
    --navy-deep: #133a66;
    --blue: #3a9be0;
    --blue-light: #5bb8ef;
    --green: #7dbb1b;
    --green-disc: #8dc814;
    --text: #4a4a4a;
    --muted: #8a8a8a;
    --icon-line: #b9b9b9;
    --ink: #1a1a1a;
    --white: #ffffff;
  }
  * { box-sizing: border-box; margin: 0; padding: 0; }
  html, body { width: 1200px; height: 900px; overflow: hidden; }
  body {
    font-family: "Lato", sans-serif;
    background: #f2f2f2;
  }
  .slide {
    position: relative;
    width: 1200px;
    height: 900px;
    overflow: hidden;
    background: radial-gradient(ellipse at 80% 25%, #ffffff 0%, #f6f6f6 45%, #ececec 100%);
  }
  .corner-mark { position: absolute; left: 0; top: 40px; }
  .slide-title {
    position: absolute;
    left: 94px;
    top: 42px;
    font-size: 56px;
    font-weight: 300;
    color: var(--navy);
    letter-spacing: -0.3px;
    white-space: nowrap;
  }
  .slide-title strong { font-weight: 700; }

  .connect { position: absolute; left: 1002px; top: 28px; }
  .connect-label {
    font-size: 14px;
    color: var(--muted);
    letter-spacing: 0.3px;
  }
  .connect-icons { display: flex; gap: 6px; margin-top: 8px; }
  .connect-icon {
    width: 36px; height: 36px;
    border: 2px solid var(--icon-line);
    border-radius: 7px;
  }

  .section { position: absolute; left: 100px; }
  .section-heading {
    font-size: 35px;
    font-weight: 300;
    white-space: nowrap;
    margin-bottom: 16px;
  }
  .section-heading strong { font-weight: 700; }
  .section--blue { top: 173px; }
  .section--blue .section-heading { color: var(--blue); }
  .section--green { top: 448px; left: 106px; }
  .section--green .section-heading { color: var(--green); }

  .bullets { list-style: none; margin-left: 48px; }
  .section--green .bullets { margin-left: 42px; }
  .bullets li {
    position: relative;
    padding-left: 32px;
    font-size: 20px;
    font-weight: 400;
    color: var(--text);
    line-height: 33.5px;
    white-space: nowrap;
  }
  .bullets li::before {
    content: "";
    position: absolute;
    left: 6px;
    top: 13px;
    width: 18px;
    height: 10px;
    clip-path: polygon(0 0, 78% 0, 100% 50%, 78% 100%, 0 100%);
  }
  .section--blue .bullets li::before { background: var(--blue); }
  .section--green .bullets li::before { background: var(--green); }

  .feature-art {
    position: absolute;
    left: 725px;
    top: 219px;
    width: 438px;
    height: 438px;
    border-radius: 50%;
    background: radial-gradient(circle at 45% 40%, #9ad21c 0%, var(--green-disc) 60%, #7fb512 100%);
  }

  .footer { position: absolute; left: 0; top: 801px; width: 1200px; height: 99px; }
  .footer-bands { position: absolute; inset: 0; }
  .brand-name {
    position: absolute;
    left: 48px;
    top: 26px;
    font-size: 44px;
    font-weight: 900;
    color: var(--white);
    letter-spacing: 0.5px;
  }
  .footer-meta {
    position: absolute;
    left: 414px;
    top: 36px;
    font-size: 16px;
    line-height: 20px;
    color: var(--white);
  }
  .page-number {
    position: absolute;
    left: 1117px;
    top: 29px;
    width: 45px;
    height: 45px;
    border: 2px solid var(--white);
    border-radius: 7px;
    color: var(--white);
    font-size: 20px;
    font-weight: 700;
    display: flex;
    align-items: center;
    justify-content: center;
  }
</style>
</head>
<body>
<main class="slide">
  <svg class="corner-mark" width="66" height="56" viewBox="0 0 66 56" aria-hidden="true">
    <polygon points="0,0 46,0 34,26 0,26" fill="var(--navy-deep)"/>
    <polygon points="14,14 64,14 50,54 0,54 0,26 10,26" fill="var(--blue)"/>
  </svg>

  <h1 class="slide-title">Single Column <strong>Bulleted List</strong></h1>

  <aside class="connect">
    <p class="connect-label">CONNECT WITH US:</p>
    <div class="connect-icons">
      <span class="connect-icon"></span>
      <span class="connect-icon"></span>
      <span class="connect-icon"></span>
      <span class="connect-icon"></span>
      <span class="connect-icon"></span>
    </div>
  </aside>

  <section class="section section--blue">
    <h2 class="section-heading"><strong>Maecenas</strong> porttitor arcu <strong>eget vehicula:</strong></h2>
    <ul class="bullets">
      <li>Nam tempor sem quis nisi imperdiet imperdiet.</li>
      <li>In auctor dui nec ante tincidunt interdum.</li>
      <li>Sed ultricies ligula a nunc volutpat vehicula.</li>
      <li>Nunc tincidunt lorem non hendrerit tempor.</li>
      <li>Quisque non lorem consequat</li>
    </ul>
  </section>

  <section class="section section--green">
    <h2 class="section-heading"><strong>Ut vel</strong> leo nec nunc <strong>interdum:</strong></h2>
    <ul class="bullets">
      <li>Phasellus feugiat justo a metus gravida sodales.</li>
      <li>Nunc quis urna sed metus consectetur mattis.</li>
      <li>Aliquam ac massa et erat scelerisque mollis.</li>
      <li>Sed in urna auctor, pretium mauris in, tristique sem.</li>
      <li>Aliquam et justo ut sem mattis sodales id vitae ipsum.</li>
    </ul>
  </section>

  <div class="feature-art" role="img" aria-label="Flat illustration of a hand holding a stopwatch reading 85 percent on a green disc"></div>

  <footer class="footer">
    <svg class="footer-bands" width="1200" height="99" viewBox="0 0 1200 99" aria-hidden="true">
      <rect x="0" y="0" width="1200" height="99" fill="var(--blue)"/>
      <polygon points="0,0 388,0 336,99 0,99" fill="var(--navy-deep)"/>
      <polygon points="328,0 388,0 358,42" fill="var(--ink)"/>
      <polygon points="336,99 380,18 400,60 380,99" fill="var(--blue-light)"/>
      <polygon points="352,99 380,50 410,99" fill="#d9eefb"/>
    </svg>
    <span class="brand-name">Veltrani</span>
    <div class="footer-meta">
      <p>19 MAY 2014</p>
      <p>Public &nbsp;|&nbsp; Copyright © 2014 Veltrani</p>
    </div>
    <div class="page-number">3</div>
  </footer>
</main>
</body>
</html>
```